LETTERHEAD & ENVELOPE: eye-catching stationary design for our custom office furniture business

Our company recently rebranded and we are in need of new stationary. Specifically, we need branded letterhead for standard paper size (8.5” x 11”), and matching envelopes, size: #9.

All designs should incorporate our brand colors, brand typeface, and logo. Please view attached brand guidelines document for brand colors, and brand description.

Letterhead: 8.5” x 11” Must include CoralvexKTN Logo, Dorrit Falke Certified Dealer Logo, mailing address, phone number, website, and email address.

Envelope: 9.5” x 4.125” Must include CoralvexKTN Logo, mailing address, and Dorrit Falke Certified Dealer Logo.

Attached files include:

```html
<!DOCTYPE html>
<html lang="en">
<head>
<meta charset="utf-8">
<title>CoralvexKTN Stationery</title>
<link rel="stylesheet" href="https://fonts.googleapis.com/css2?family=Raleway:wght@300;400;700;800&family=Lato:wght@300;400&display=swap">
<style>
  :root {
    --backdrop: #d9e4ef;
    --paper: #ffffff;
    --brand-green: #5a8070;
    --ink: #58595b;
    --ink-dark: #4d4d4f;
    --dealer-red: #e8391f;
    --bar-grey: #a7a7ab;
    --shadow: 2px 3px 6px rgba(60, 70, 85, 0.35);
  }
  * { margin: 0; padding: 0; box-sizing: border-box; }
  html, body { width: 1200px; height: 831px; overflow: hidden; }
  body { background: var(--backdrop); position: relative; font-family: "Lato", sans-serif; color: var(--ink); }

  .sheet { position: absolute; background: var(--paper); box-shadow: var(--shadow); }

  /* Letterhead */
  .letterhead { left: 117px; top: 111px; width: 430px; height: 609px; }
  .brand { position: absolute; display: flex; align-items: center; gap: 10px; }
  .brand-dot { width: 29px; height: 29px; border-radius: 50%; background: var(--brand-green); flex: none; }
  .brand-name { font-family: "Raleway", sans-serif; font-weight: 400; font-size: 24px; color: var(--brand-green); letter-spacing: 0.2px; }
  .letterhead .brand { left: 40px; top: 47px; }

  .contact { position: absolute; left: 305px; top: 34px; font-family: "Lato", sans-serif; font-size: 8px; line-height: 10px; color: var(--ink); }
  .contact .address { margin-bottom: 4px; }
  .contact-row { display: flex; align-items: center; height: 11px; }
  .contact-row svg { width: 8px; height: 8px; margin-right: 7px; flex: none; }

  .date { position: absolute; left: 40px; top: 208px; font-family: "Raleway", sans-serif; font-size: 10px; color: var(--ink); }
  .recipient { position: absolute; left: 40px; top: 225px; font-family: "Raleway", sans-serif; font-weight: 800; font-size: 15px; color: var(--ink-dark); letter-spacing: 0.2px; }
  .recipient-role { position: absolute; left: 40px; top: 247px; font-family: "Raleway", sans-serif; font-weight: 300; font-size: 10px; color: var(--ink); }

  .body-copy { position: absolute; left: 40px; top: 285px; width: 349px; font-size: 7.6px; line-height: 15px; text-align: justify; color: var(--ink); }
  .body-copy p { margin-bottom: 15px; }
  .body-copy p.last { text-align: left; }

  .signoff { position: absolute; left: 40px; top: 452px; font-size: 9px; color: var(--ink); }
  .signature { position: absolute; left: 40px; top: 475px; width: 46px; height: 34px; background: linear-gradient(135deg, #e6eeeb, #cfdcd6); border-radius: 3px; }

  .dealer { position: absolute; display: flex; align-items: center; gap: 8px; }
  .dealer-dot { border-radius: 50%; background: var(--dealer-red); flex: none; }
  .dealer-name { font-family: "Lato", sans-serif; font-weight: 400; color: var(--dealer-red); white-space: nowrap; }
  .letterhead .dealer { left: 136px; top: 567px; }
  .letterhead .dealer-dot { width: 23px; height: 23px; }
  .letterhead .dealer-name { font-size: 11px; }

  .footer-bar { position: absolute; left: 0; bottom: 0; width: 100%; height: 7px; display: flex; }
  .footer-bar .green { background: var(--brand-green); }
  .footer-bar .gap { background: var(--paper); width: 3px; }
  .footer-bar .grey { background: var(--bar-grey); flex: 1; }
  .letterhead .footer-bar .green { width: 353px; }

  /* Envelope back */
  .envelope-back { left: 635px; top: 157px; width: 451px; height: 225px; }
  .flap { position: absolute; left: 0; top: 0; width: 451px; height: 66px; }

  /* Envelope front */
  .envelope-front { left: 635px; top: 448px; width: 451px; height: 226px; }
  .envelope-front .brand { left: 45px; top: 48px; }
  .return-address { position: absolute; left: 45px; top: 173px; padding-left: 8px; border-left: 1.5px solid var(--brand-green); font-family: "Lato", sans-serif; font-size: 10.5px; line-height: 12px; color: var(--ink); }
  .envelope-front .dealer { left: 285px; top: 174px; }
  .envelope-front .dealer-dot { width: 20px; height: 20px; }
  .envelope-front .dealer-name { font-size: 9.5px; }
  .envelope-front .footer-bar { height: 6px; }
  .envelope-front .footer-bar .green { width: 371px; }
</style>
</head>
<body>

  <section class="sheet letterhead" aria-label="Letterhead">
    <div class="brand">
      <span class="brand-dot"></span>
      <span class="brand-name">CoralvexKTN</span>
    </div>

    <div class="contact">
      <div class="address">418 NW Larkspur, Suite 140<br>Brenwood, OR 97019</div>
      <div class="contact-row">
        <svg viewBox="0 0 10 10" aria-hidden="true"><path d="M2 1 L4 3 L3 4.2 Q4 6 5.8 7 L7 6 L9 8 L7.6 9.2 Q3.5 8.5 0.8 2.4 Z" fill="var(--brand-green)"/></svg>
        555.014.2286
      </div>
      <div class="contact-row">
        <svg viewBox="0 0 10 10" aria-hidden="true"><rect x="0.5" y="2" width="9" height="6.5" fill="var(--brand-green)"/><path d="M0.8 2.3 L5 5.6 L9.2 2.3" fill="none" stroke="#fff" stroke-width="0.9"/></svg>
        info@coralvexktn.com
      </div>
      <div class="contact-row">
        <svg viewBox="0 0 10 10" aria-hidden="true"><circle cx="5" cy="5" r="4.3" fill="none" stroke="var(--brand-green)" stroke-width="0.9"/><ellipse cx="5" cy="5" rx="1.9" ry="4.3" fill="none" stroke="var(--brand-green)" stroke-width="0.8"/><path d="M0.7 5 H9.3" stroke="var(--brand-green)" stroke-width="0.8"/></svg>
        www.coralvexktn.com
      </div>
    </div>

    <div class="date">01 December, 2021</div>
    <div class="recipient">DANIEL HARROW</div>
    <div class="recipient-role">Cheif Executive Officer</div>

    <div class="body-copy">
      <p>Contrary to popular belief, Lorem Ipsum is not simply random text. It has roots in a piece of classical Latin literature from 45 BC, making it over 2000 years old. Edwin Calloway, a Latin professor at Marlow Ridge College in Virginia, looked up one of the more obscure Latin words, consectetur.</p>
      <p>Lorem Ipsum comes from sections 1.10.32 and 1.10.33 of "de Finibus Bonorum et Malorum" (The Extremes of Good and Evil) by Aurelian, written in 45 BC. This book is a treatise on the theory of ethics, very popular during the Renaissance. The first line of Lorem Ipsum.</p>
      <p class="last">The standard chunk of Lorem Ipsum used since the 1500s is reproduced below for those interested.</p>
    </div>

    <div class="signoff">Best Regards</div>
    <div class="signature" role="img" aria-label="Handwritten signature"></div>

    <div class="dealer">
      <span class="dealer-dot"></span>
      <span class="dealer-name">Dorrit Falke Certified Dealer</span>
    </div>

    <div class="footer-bar"><span class="green"></span><span class="gap"></span><span class="grey"></span></div>
  </section>

  <section class="sheet envelope-back" aria-label="Envelope back">
    <svg class="flap" viewBox="0 0 451 66" aria-hidden="true">
      <path d="M0 0 H451 L447 40 Q444 66 418 66 H33 Q7 66 4 40 Z" fill="var(--brand-green)"/>
      <circle cx="226" cy="33" r="19" fill="#ffffff"/>
    </svg>
  </section>

  <section class="sheet envelope-front" aria-label="Envelope front">
    <div class="brand">
      <span class="brand-dot"></span>
      <span class="brand-name">CoralvexKTN</span>
    </div>

    <div class="return-address">418 NW Larkspur, Suite 140<br>Brenwood, OR 97019</div>

    <div class="dealer">
      <span class="dealer-dot"></span>
      <span class="dealer-name">Dorrit Falke Certified Dealer</span>
    </div>

    <div class="footer-bar"><span class="green"></span><span class="gap"></span><span class="grey"></span></div>
  </section>

</body>
</html>
```